Email Banner - TevonQuarry.com

I need an email banner created for my website: Tevonquarry.com.
The logos are attatched here and an example of an email banner we have used in the past is also attatched. Please keep the tagline: "Essential Whitepapers for Business Professionals" - The logos are in the framebazaar zip folder.

Tevonquarry

```html
<!DOCTYPE html>
<html lang="en">
<head>
<meta charset="UTF-8">
<title>Tevonquarry Email Banner</title>
<link rel="stylesheet" href="https://fonts.googleapis.com/css2?family=Figtree:wght@400;500;700;800&display=swap">
<style>
  :root {
    --page-bg: #eef0f4;
    --navy: #243080;
    --royal: #2f47c4;
    --bright-blue: #3d6ef5;
    --sky: #aabff8;
    --white: #ffffff;
    --brand-ink: #26358f;
  }
  html, body {
    margin: 0;
    padding: 0;
    width: 1200px;
    height: 1200px;
    overflow: hidden;
    background: var(--page-bg);
  }
  .canvas {
    position: relative;
    width: 1200px;
    height: 1200px;
    background: var(--page-bg);
  }
  .banner {
    position: absolute;
    left: 117px;
    top: 524px;
    width: 965px;
    height: 151px;
    overflow: hidden;
    background: linear-gradient(90deg, var(--royal) 0%, var(--royal) 45%, var(--navy) 78%, var(--navy) 100%);
    font-family: "Figtree", sans-serif;
  }
  .brand-panel {
    position: absolute;
    left: 0;
    top: 0;
    width: 470px;
    height: 151px;
  }
  .brand-name {
    position: absolute;
    left: 0;
    top: 0;
    width: 420px;
    height: 151px;
    display: flex;
    align-items: center;
    justify-content: center;
    margin: 0;
    font-size: 40px;
    font-weight: 700;
    letter-spacing: -0.5px;
    color: var(--brand-ink);
  }
  .tagline {
    position: absolute;
    left: 457px;
    top: 44px;
    margin: 0;
    color: var(--white);
    font-size: 26px;
    line-height: 35px;
    font-weight: 400;
  }
  .tagline strong {
    font-weight: 700;
  }
  .cta {
    position: absolute;
    right: 0;
    top: 0;
    width: 169px;
    height: 55px;
    display: flex;
    align-items: center;
    justify-content: center;
    background: var(--bright-blue);
    border-bottom-left-radius: 22px;
    color: var(--white);
    font-size: 19px;
    font-weight: 700;
    letter-spacing: 0.3px;
    text-decoration: none;
  }
</style>
</head>
<body>
  <div class="canvas">
    <div class="banner">
      <svg class="brand-panel" viewBox="0 0 470 151" aria-hidden="true">
        <defs>
          <linearGradient id="band-fill" x1="0" y1="0" x2="0" y2="1">
            <stop offset="0" stop-color="#aabff8"/>
            <stop offset="1" stop-color="#3d6ef5"/>
          </linearGradient>
        </defs>
        <path d="M0 0 H362 C430 22 458 84 448 151 H0 Z" fill="url(#band-fill)"/>
        <path d="M0 0 H40 L0 40 Z" fill="#3d6ef5"/>
        <path d="M0 58 C18 32 46 12 70 0 H342 C398 24 426 84 417 151 H0 Z" fill="#ffffff"/>
      </svg>
      <p class="brand-name">Tevonquarry</p>
      <p class="tagline">Essential Whitepapers<br>for <strong>Business Professionals</strong></p>
      <a class="cta" href="#">CLICK HERE</a>
    </div>
  </div>
</body>
</html>
```